Business Card design for construction company

I would like a business card design for a construction company - ORD Builders. I have attached the ai logo file for use. I would like the card to be very smart and clean and incorporate only white and the two colours in the logo. I would like the card to have two sides. One side can just have the logo, the other with the relevant information.

Target Market(s)

Building and Construction Clients

Industry/Entity Type

Business

Contact Information for Business Card

Name: Tom Harcliffe
Company: ORD Builders Pty Limited
Address: 14 Mulberry Crescent Oakvale Heights 2093
Phone: 0432 517 208
Email: tomh@ordbuilders.example.au

Font styles to use
Serif
Sans Serif

Requirements
Must have
• Details noted above
• Logo as provided
• Colours as in logo
• Square edges
• A font that compliments the logo
Should not have
• Any colour other than white and those in logo
• Rounded edges

```html
<!DOCTYPE html>
<html lang="en">
<head>
<meta charset="utf-8">
<title>ORD Builders – Business Card</title>
<link rel="stylesheet" href="https://fonts.googleapis.com/css2?family=Lato:ital,wght@0,400;0,700;1,400;1,700&display=swap">
<style>
  :root {
    --stage: #2e2e30;
    --slate: #555557;
    --slate-dark: #4a4a4c;
    --brand-blue: #1a9ee0;
    --paper: #ffffff;
    --ink: #222224;
    --logo-grey: #5a5a5c;
  }
  * { margin: 0; padding: 0; box-sizing: border-box; }
  html, body {
    width: 1200px; height: 900px; overflow: hidden;
    background: var(--stage);
    font-family: "Lato", Arial, sans-serif;
  }
  .stage {
    width: 1200px; height: 900px;
    display: flex; align-items: center; justify-content: center; gap: 40px;
  }
  .card {
    position: relative;
    width: 540px; height: 330px;
    overflow: hidden;
    box-shadow: 0 10px 30px rgba(0,0,0,.45);
  }
  .card--front { background: var(--paper); }
  .card--back {
    background: var(--slate);
    display: flex; align-items: center; justify-content: center;
  }
  .wordmark {
    display: flex; align-items: center; gap: 12px;
    font-weight: 400; letter-spacing: 3px; text-transform: uppercase;
  }
  .wordmark__dot { width: 9px; height: 9px; background: var(--brand-blue); }
  .card--front .wordmark {
    position: absolute; left: 40px; top: 42px;
    font-size: 30px; color: var(--logo-grey);
  }
  .card--back .wordmark { font-size: 36px; color: var(--paper); }

  .contact {
    position: absolute; left: 40px; top: 118px;
    color: var(--ink); font-style: italic; font-size: 15px; line-height: 1.3;
  }
  .contact__phone { display: flex; align-items: center; gap: 10px; margin-bottom: 14px; }
  .contact__phone svg { width: 12px; height: 14px; }
  .holder-name {
    position: absolute; right: 50px; top: 218px;
    color: var(--brand-blue); font-weight: 700; font-style: italic; font-size: 26px;
  }
  .footer-band { position: absolute; inset: 0; width: 540px; height: 330px; }
  .email {
    position: absolute; right: 36px; bottom: 10px;
    color: var(--paper); font-style: italic; font-size: 15px; letter-spacing: .3px;
  }
</style>
</head>
<body>
<main class="stage">
  <section class="card card--front" aria-label="Business card, details side">
    <svg class="footer-band" viewBox="0 0 540 330" aria-hidden="true">
      <path d="M0,250 C150,262 330,302 540,286 L540,330 L0,330 Z" fill="var(--slate-dark)"/>
      <path d="M0,250 C150,262 330,302 540,286" fill="none" stroke="var(--paper)" stroke-width="6"/>
      <path d="M60,253 C210,268 370,292 540,264 L540,280 C370,300 210,276 60,253 Z" fill="var(--brand-blue)"/>
    </svg>
    <div class="wordmark"><span class="wordmark__dot"></span>ORD Builders</div>
    <div class="contact">
      <p class="contact__phone">
        <svg viewBox="0 0 12 14" aria-hidden="true"><path d="M3 1 L5 4 L3.6 5.4 C4.4 7.4 5.6 8.8 7.2 9.8 L8.6 8.6 L11 10.8 L9.6 13 C5 12.4 1.2 7.6 1 2.6 Z" fill="var(--brand-blue)"/></svg>
        0432 517 208
      </p>
      <p>ORD Builders Pty Limited</p>
      <p>14 Mulberry Crescent</p>
      <p>Oakvale Heights 2093</p>
    </div>
    <p class="holder-name">Tom Harcliffe</p>
    <p class="email">tomh@ordbuilders.example.au</p>
  </section>

  <section class="card card--back" aria-label="Business card, brand side">
    <div class="wordmark"><span class="wordmark__dot"></span>ORD Builders</div>
  </section>
</main>
</body>
</html>
```